Harrowgate Legal

To update and modernize current business card appearance. Marisa's business is based in Melbourne with 4 other lawyers in the firm. Marisa travels to the Pilbara in Western Australia approximately 1 week a month as part of the firms legal work. She consults with clients in Newman, Tom Price and Port Hedland. The lawyers work mostly from a home office, apart from court appearances. They have a virtual office in Melbourne city, and use facilities in 3 or 4 other locations around Melbourne. It is important the client's think this is a conventional law firm with a permanent office. Our business structure is a difficult concept for them to grasp. The business has been operational for 3 years, growing from 1 lawyer to 4 lawyers during that time. Our website is www.Harrowgatelegal.com.au and is currently being upgraded as we are not happy with its content. The logo is currently orange and dark grey but the orange is a difficult colour to reproduce and often turns out "poo" brown when documents are printed. We need clients to know we are user friendly and caring - and not head up our rears ends as some lawyers appear to be.
Updates

Thank you for the feedback so far. 1. Some of the designs have too much black (We prefer darker grey & not too much.) 2. Happy for designers to play around with different colours & logo design. What we're after is a modern look and business card that people say "wow" when they pick it up.

Industry/Entity Type

Business

```html
<!DOCTYPE html>
<html lang="en">
<head>
<meta charset="utf-8">
<title>Harrowgate Legal – Business Card</title>
<link rel="stylesheet" href="https://fonts.googleapis.com/css2?family=Open+Sans:wght@400;600;700&display=swap">
<style>
  :root {
    --royal-blue: #2a3f9e;
    --deep-blue: #22358c;
    --accent-orange: #f05a22;
    --ink: #1e1e1e;
    --slate: #555a66;
    --paper: #ffffff;
    --backdrop: #ece9e4;
    --mist: #e9eaf4;
  }
  * { box-sizing: border-box; margin: 0; padding: 0; }
  html, body { width: 1200px; height: 1023px; overflow: hidden; }
  body {
    background: var(--backdrop);
    font-family: "Open Sans", Arial, sans-serif;
    position: relative;
  }
  .card {
    position: absolute;
    width: 540px;
    height: 310px;
    overflow: hidden;
    box-shadow: 0 6px 18px rgba(0,0,0,.18);
  }

  /* Front */
  .card-front { left: 70px; top: 90px; background: var(--paper); }
  .front-ring {
    position: absolute; right: 60px; top: -60px;
    width: 260px; height: 260px; border-radius: 50%;
    border: 26px solid var(--mist);
  }
  .brand {
    position: absolute; right: 40px; top: 44px;
    display: flex; align-items: center; gap: 10px;
    color: var(--slate); font-weight: 600; font-size: 24px;
    letter-spacing: 2px; text-transform: uppercase;
  }
  .brand-dot { width: 26px; height: 26px; border-radius: 50%; background: var(--royal-blue); }
  .brand-rule {
    position: absolute; right: 40px; top: 86px;
    width: 250px; height: 2px; background: var(--slate);
  }
  .name-tab {
    position: absolute; left: 0; top: 128px;
    width: 40px; height: 40px; background: var(--accent-orange);
  }
  .identity { position: absolute; left: 56px; top: 118px; }
  .person-name { color: var(--royal-blue); font-weight: 700; font-size: 28px; line-height: 1.1; }
  .credentials { color: var(--ink); font-size: 11px; margin-top: 3px; }
  .role { color: var(--ink); font-weight: 700; font-size: 16px; margin-top: 2px; }
  .contacts { position: absolute; left: 190px; top: 200px; list-style: none; }
  .contacts li {
    display: flex; align-items: center; gap: 8px;
    color: var(--ink); font-size: 15px; line-height: 21px;
  }
  .contacts svg { width: 13px; height: 13px; flex: none; }
  .front-band {
    position: absolute; left: 0; right: 0; bottom: 0; height: 30px;
    background: var(--royal-blue); border-top: 3px solid var(--accent-orange);
  }

  /* Back */
  .card-back { left: 590px; top: 600px; background: var(--royal-blue); }
  .back-ring {
    position: absolute; left: 230px; top: -90px;
    width: 300px; height: 300px; border-radius: 50%;
    border: 30px solid var(--deep-blue);
  }
  .practice { position: absolute; left: 40px; top: 50px; color: var(--paper); }
  .practice-title { font-weight: 700; font-size: 19px; margin-bottom: 6px; }
  .practice-list { list-style: none; }
  .practice-list > li { font-weight: 600; font-size: 17px; line-height: 22px; }
  .practice-list > li::before { content: "\2713"; font-size: 12px; margin-right: 8px; }
  .sub-list { list-style: none; font-weight: 400; font-size: 14px; line-height: 18px; padding-left: 22px; }
  .back-strip {
    position: absolute; left: 0; right: 0; bottom: 0; height: 62px;
    background: var(--paper); border-top: 3px solid var(--accent-orange);
  }
  .values {
    position: absolute; left: 26px; bottom: 12px;
    display: flex; gap: 18px; list-style: none;
    color: var(--ink); font-size: 13px;
  }
  .values li::before { content: "\2022"; margin-right: 3px; }
  .inquiries {
    position: absolute; right: 22px; bottom: 12px;
    color: var(--royal-blue); font-size: 12px;
  }
  .back-brand {
    position: absolute; right: 22px; top: 10px;
    display: flex; align-items: center; gap: 6px;
    color: var(--slate); font-weight: 600; font-size: 11px;
    letter-spacing: 1px; text-transform: uppercase;
  }
  .back-brand .brand-dot { width: 12px; height: 12px; }
</style>
</head>
<body>
  <section class="card card-front" aria-label="Business card front">
    <div class="front-ring"></div>
    <div class="brand"><span class="brand-dot"></span>Harrowgate Legal</div>
    <div class="brand-rule"></div>
    <div class="name-tab"></div>
    <div class="identity">
      <h1 class="person-name">J.Marisa Thornbury</h1>
      <p class="credentials">LLB(Hones) - Accredited Mediator</p>
      <p class="role">Principal Solicitor</p>
    </div>
    <ul class="contacts">
      <li><svg viewBox="0 0 16 16"><path d="M4 1l3 3-2 2c1 2 3 4 5 5l2-2 3 3-2 3C7 15 1 9 1 3z" fill="#f05a22"/></svg>1300 Harrowgate (427 764)</li>
      <li><svg viewBox="0 0 16 16"><rect x="2" y="1" width="12" height="14" rx="1" fill="none" stroke="#f05a22" stroke-width="2"/></svg>0412 555 019</li>
      <li><svg viewBox="0 0 16 16"><rect x="1" y="3" width="14" height="10" fill="#f05a22"/><path d="M1 3l7 6 7-6" fill="none" stroke="#fff" stroke-width="1.5"/></svg>marisa.thornbury@harrowgatelegal.com.au</li>
    </ul>
    <div class="front-band"></div>
  </section>

  <section class="card card-back" aria-label="Business card back">
    <div class="back-ring"></div>
    <div class="practice">
      <h2 class="practice-title">AREAS OF PARCTICE:</h2>
      <ul class="practice-list">
        <li>Family Law
          <ul class="sub-list">
            <li>Collaborative Practice</li>
            <li>Mediation &amp; Negotiation</li>
            <li>Intervention Orders</li>
          </ul>
        </li>
        <li>Criminal Law</li>
      </ul>
    </div>
    <div class="back-strip">
      <ul class="values">
        <li>Experience</li>
        <li>Support</li>
        <li>Solutions</li>
      </ul>
      <div class="back-brand"><span class="brand-dot"></span>Harrowgate Legal</div>
      <p class="inquiries">Inquiries: info@harrowgatelegal.com.au</p>
    </div>
  </section>
</body>
</html>
```